Business Card Design Project : Tidewell Press

In preparation for market launch, Whistler's Tidewell Press require the development of a business card. Tidewell Press is a Community online publishing web portal. We provide the the city of Whistler located in B.C. (Canada) business directories, News, Classified ads, News, Events and blogs etc.

The main focus of the brand is to help local businesses to corporate with their online advertisement and marketing. Meeting our clients face to face is a must (B2B).

Target Market(s)

The target market is B2B customers. Business Owners to Marketing, advertising Managers

Industry/Entity Type

Business

Requirements
Must have
• - The business card will be two sided.
the BACK side will have our logo which consist of (icon, url,slogan) submited. The logo will be middle and centred.

The FRONT side should have company details:

Company Legal Name: FERNDALE TIDEWELL PRESS

Owen Marsk
Director of Sales & Marketing

www.ferndaletidewell.biz
owen@ferndaletidewell.biz

Phone: 555 014 3826
#2817 - 562 E. Harlow Ave.
Vancouver, B.C. K7P2R4 Canada
Nice to have
• - For the "FRONT" side of our business card. You can separate or re-arrange with our logo components (icon, logo,slogan). It does not have to be together.

Also our company legal name is rather long so arrange or organize the name in a way to make it shorter. Your experience and creativity will have to come in play.
Should not have
• should not have other colors beside logo color and black text (2 colors). Also nothing Three dimensional

```html
<!DOCTYPE html>
<html lang="en">
<head>
<meta charset="utf-8">
<title>Tidewell Press — Business Card</title>
<link rel="stylesheet" href="https://fonts.googleapis.com/css2?family=Source+Sans+3:ital,wght@0,400;0,600;1,400;1,700&display=swap">
<style>
  :root {
    --brand-blue: #2a8ad4;
    --ink: #111111;
    --card-paper: #fbfbfb;
    --backdrop: #1c1c1c;
  }
  * { margin: 0; padding: 0; box-sizing: border-box; }
  html, body {
    width: 1200px; height: 848px; overflow: hidden;
    background: var(--backdrop);
    font-family: "Source Sans 3", "Myriad Pro", sans-serif;
  }
  .stage {
    width: 1200px; height: 848px;
    display: flex; align-items: center; justify-content: center; gap: 40px;
  }
  .card {
    position: relative;
    width: 560px; height: 320px;
    background: var(--card-paper);
  }

  /* Front side */
  .card--front .contact {
    position: absolute; left: 0; top: 0; width: 290px; height: 100%;
    display: flex; flex-direction: column; align-items: center; justify-content: center;
    text-align: center; color: var(--ink);
  }
  .contact__name {
    font-size: 42px; font-weight: 400; color: var(--brand-blue); line-height: 1;
    margin-bottom: 8px;
  }
  .contact__title { font-size: 14px; font-weight: 700; font-style: italic; margin-bottom: 4px; }
  .contact__email { font-size: 9px; font-style: italic; color: var(--brand-blue); }
  .contact__web { font-size: 9px; font-style: italic; margin-bottom: 18px; }
  .contact__details { font-size: 13px; line-height: 1.35; }

  .divider {
    position: absolute; left: 290px; top: 46px; width: 3px; height: 230px;
    background: var(--brand-blue);
  }

  .card--front .brand {
    position: absolute; left: 293px; right: 0; top: 0; height: 100%;
    display: flex; flex-direction: column; align-items: center; justify-content: center;
  }
  .brand__mark { width: 18px; height: 18px; background: var(--brand-blue); margin-bottom: 8px; }
  .brand__name {
    font-size: 16px; font-weight: 400; color: var(--ink);
    text-align: center; line-height: 1.05; letter-spacing: 0.02em;
  }
  .brand__slogan { margin-top: 10px; font-size: 13px; color: var(--brand-blue); }

  /* Back side */
  .card--back .brand {
    position: absolute; inset: 0;
    display: flex; flex-direction: column; align-items: center; justify-content: center;
  }
  .brand__row { display: flex; align-items: center; gap: 12px; }
  .brand__row .brand__mark { width: 22px; height: 22px; margin: 0; }
  .brand__url { font-size: 29px; font-weight: 400; color: var(--ink); }
  .card--back .brand__slogan { font-size: 20px; margin-top: 2px; }
</style>
</head>
<body>
  <main class="stage">
    <section class="card card--front" aria-label="Business card front">
      <div class="contact">
        <h1 class="contact__name">Owen Marsk</h1>
        <p class="contact__title">Director of Sales &amp; Marketing</p>
        <p class="contact__email">owen@ferndaletidewell.biz</p>
        <p class="contact__web">www.ferndaletidewell.biz</p>
        <p class="contact__details">
          Phone: 555 014 3826<br>
          #2817 - 562 E. Harlow Ave.<br>
          Vancouver, B.C. K7P2R4 Canada
        </p>
      </div>
      <div class="divider"></div>
      <div class="brand">
        <div class="brand__mark"></div>
        <p class="brand__name">FERNDALE<br>TIDEWELL<br>PRESS</p>
        <p class="brand__slogan">Your information gateway</p>
      </div>
    </section>

    <section class="card card--back" aria-label="Business card back">
      <div class="brand">
        <div class="brand__row">
          <div class="brand__mark"></div>
          <p class="brand__url">www.ferndaletidewell.biz</p>
        </div>
        <p class="brand__slogan">Your information gateway</p>
      </div>
    </section>
  </main>
</body>
</html>
```